Corporate Brightfen business cards to be handed to investor, bankers etc. Needs to have a young feel

I need business cards designed for a technology company that provides uber-like rapid response on the security industry. I would like it simple but very cool and tasteful. See attached documents for artwork and colours to be used. Cut sheet describes business model. Card stock should be thicker than normal. I would like the one side to be just the art and the other to have the contact info with maybe the pin somewhere.

Target Market(s)

Investors

Industry/Entity Type

Business

Contact Information for Business Card

Would like the logo attached on one side with name address and other info on the other side.

Font styles to use
Other font styles liked:
• See existing logo

Colors
6b449b
886aae
e4daeb
ffffff

Requirements
Must have
• Name: Dorian Felkatsis
• Address: 47 Larkfield Avenue, Toronto, On, M6K2B7
• Tel: 416-7291846
• Email: rolo@brightfen.io
Nice to have
• See logo colours

```html
<!DOCTYPE html>
<html lang="en">
<head>
<meta charset="utf-8">
<title>Brightfen Business Card</title>
<link href="https://fonts.googleapis.com/css2?family=Montserrat:wght@400;500&display=swap" rel="stylesheet">
<style>
  :root {
    --purple: #6b449b;
    --purple-mid: #886aae;
    --lavender: #e4daeb;
    --white: #ffffff;
    --ink: #1c1c1c;
    --text-grey: #4d4d4d;
    --backdrop: #d9d9db;
  }
  * { box-sizing: border-box; margin: 0; padding: 0; }
  html, body {
    width: 1200px; height: 900px; overflow: hidden;
    background: var(--backdrop);
    font-family: "Montserrat", sans-serif;
  }
  .sheet {
    position: relative; width: 1200px; height: 900px;
  }
  .card {
    position: absolute; left: 280px; width: 640px; height: 366px;
    background: var(--white); border-radius: 18px; overflow: hidden;
    box-shadow: 0 6px 20px rgba(0,0,0,0.18);
  }
  .card--front { top: 60px; }
  .card--back { top: 474px; }
  .card__art { position: absolute; inset: 0; width: 640px; height: 366px; }

  .wordmark {
    position: absolute; display: flex; align-items: center;
    color: var(--ink); font-weight: 400; letter-spacing: 0.5px;
    white-space: nowrap;
  }
  .wordmark__dot { border-radius: 50%; background: var(--purple-mid); flex: none; }
  .card--front .wordmark { top: 26px; right: 40px; font-size: 30px; gap: 6px; }
  .card--front .wordmark__dot { width: 14px; height: 14px; }
  .card--back .wordmark {
    top: 132px; left: 0; right: 0; justify-content: center;
    font-size: 84px; gap: 16px;
  }
  .card--back .wordmark__dot { width: 34px; height: 34px; }

  .holder-name {
    position: absolute; left: 44px; top: 112px;
    color: var(--purple-mid); font-size: 28px; font-weight: 500;
    white-space: nowrap;
  }
  .contact-list { position: absolute; left: 44px; top: 158px; list-style: none; }
  .contact-list li {
    display: flex; align-items: center; gap: 14px; height: 34px;
    color: var(--text-grey); font-size: 18px; letter-spacing: 0.6px;
    white-space: nowrap;
  }
  .contact-icon { width: 26px; height: 26px; flex: none; }
  .address {
    position: absolute; left: 180px; right: 20px; top: 300px; height: 66px;
    display: flex; align-items: center;
    color: var(--white); font-size: 17px; letter-spacing: 0.4px;
    white-space: nowrap;
  }
</style>
</head>
<body>
<main class="sheet">

  <section class="card card--front" aria-label="Card front with contact details">
    <svg class="card__art" viewBox="0 0 640 366" aria-hidden="true">
      <polygon points="0,300 150,300 136,366 0,366" fill="var(--ink)"/>
      <polygon points="162,300 640,300 640,366 148,366" fill="var(--purple-mid)"/>
      <circle cx="70" cy="334" r="9" fill="var(--white)"/>
    </svg>

    <div class="wordmark"><span class="wordmark__dot"></span>brightfen</div>

    <h1 class="holder-name">Dorian Felkatsis</h1>

    <ul class="contact-list">
      <li>
        <svg class="contact-icon" viewBox="0 0 26 26" aria-hidden="true">
          <circle cx="13" cy="13" r="11.5" fill="none" stroke="var(--purple-mid)" stroke-width="1.6"/>
          <path d="M9.5 7.5 l2 2 -1.2 1.5 c0.8 1.8 2 3 3.8 3.8 l1.5-1.2 2 2 -1.6 1.6 c-3.8-0.6-7.5-4.3-8.1-8.1z" fill="var(--purple-mid)"/>
        </svg>
        <span>416-7291846</span>
      </li>
      <li>
        <svg class="contact-icon" viewBox="0 0 26 26" aria-hidden="true">
          <circle cx="13" cy="13" r="11.5" fill="none" stroke="var(--purple-mid)" stroke-width="1.6"/>
          <rect x="7" y="9" width="12" height="8.5" fill="none" stroke="var(--purple-mid)" stroke-width="1.4"/>
          <path d="M7 9 l6 5 6-5" fill="none" stroke="var(--purple-mid)" stroke-width="1.4"/>
        </svg>
        <span>rolo@brightfen.io</span>
      </li>
      <li>
        <svg class="contact-icon" viewBox="0 0 26 26" aria-hidden="true">
          <circle cx="13" cy="13" r="11.5" fill="none" stroke="var(--purple-mid)" stroke-width="1.6"/>
          <circle cx="13" cy="13" r="6.5" fill="none" stroke="var(--purple-mid)" stroke-width="1.3"/>
          <ellipse cx="13" cy="13" rx="2.8" ry="6.5" fill="none" stroke="var(--purple-mid)" stroke-width="1.2"/>
          <path d="M6.5 13 h13 M7.5 10 h11 M7.5 16 h11" stroke="var(--purple-mid)" stroke-width="1.1"/>
        </svg>
        <span>www.brightfen.io</span>
      </li>
    </ul>

    <p class="address">47 Larkfield Avenue, Toronto, On, M6K2B7</p>
  </section>

  <section class="card card--back" aria-label="Card back with brand name">
    <svg class="card__art" viewBox="0 0 640 366" aria-hidden="true">
      <polygon points="0,40 190,40 180,62 0,62" fill="var(--purple-mid)"/>
      <polygon points="0,66 178,66 174,74 0,74" fill="var(--purple-mid)"/>
      <polygon points="470,292 640,292 640,300 466,300" fill="var(--purple-mid)"/>
      <polygon points="464,304 640,304 640,326 454,326" fill="var(--purple-mid)"/>
    </svg>
    <div class="wordmark"><span class="wordmark__dot"></span>brightfen</div>
  </section>

</main>
</body>
</html>
```